Wordpress Contest Brief I would like a WordPress theme designed

Industry / Entity Type

Financial consultancy / advisers

Current site is: http://www.quorvel-group.com

Looking for a complete overhaul of this site, we are after a clean modern look. Will require the ability to easily add, update and remove content, hence the WordPress design.
Example:
Add case studies
Industry documentation (downloadable brochures / flyers and such)

What we like from our current site is the colour the fonts and the logo (the city of London) we would like to have other city outlines (NYC and Tokyo, Hong Kong, Singapore).

The site will be used by our potential clients to get in contact and re-view the case studies, if possible would like to have a client login area where they can download our documents like NDA’s etc and T&C’s.

Task Outline

Create a Web Design (Coded - Design and coding required)
Designer must provide full implementation/coding depending on the platform chosen by the client (i.e. WordPress theme, HTML/CSS, bootstrap etc.)

Task Description

I need a full website built that must work on desktop and mobile. I can provide the London city skyline and the font file, which we have used. Some stock industrial photos will be required.

Requirements:

*Splash page
*What We Do
*How We do it
*Who Are We? To have the same information and links as the current site
*Why use us?
*Clients: To have the same information and links as the current site
*Partners: To have the same information and links as the current site
*Contact:

Target Market(s)

Financial institutions trading Equities, Futures, Options, Forex and Fixed Income.
Regulators, Exchanges, ECN’s
Buy side firms and Sell side firms

Industry/Entity Type

Financial

Coding

Coded - Design and coding required

Number of Pages Required

5+ page

Font styles to use
Sans Serif

Colors
f04a50

Requirements
Must have
• Splash page
• What We Do
• How We do it
• Who Are We? To have the same information and links as the current site
• Why use us?
• Clients: To have the same information and links as the current site
• Partners: To have the same information and links as the current site
• Contact:

```html
<!DOCTYPE html>
<html lang="en">
<head>
<meta charset="utf-8">
<title>Quorvel Advisers</title>
<link href="https://fonts.googleapis.com/css2?family=Open+Sans:wght@400;600;700&display=swap" rel="stylesheet">
<style>
:root{
  --red:#f04a50;
  --ink:#1e1e1e;
  --text:#333;
  --muted:#555;
  --pale:#e4e4e8;
  --card:#a8a8a8;
  --foot:#e6e6ea;
  --bar:#8a8a8a;
  --white:#fff;
}
*{box-sizing:border-box;margin:0;padding:0}
html,body{width:1200px;height:3734px;overflow:hidden}
body{font-family:"Open Sans",Arial,sans-serif;color:var(--text);background:var(--white);position:relative}
.btn{position:absolute;background:var(--red);color:var(--white);font-size:15px;text-transform:uppercase;display:flex;align-items:center;justify-content:center;letter-spacing:.3px}

/* header + hero */
.hero{position:absolute;left:0;top:0;width:1200px;height:585px;background:linear-gradient(90deg,#f3f3f5 0%,#ececef 30%,#cfd3da 55%,#b9c0ca 80%,#d6d9de 100%)}
.hero-photo{position:absolute;left:380px;top:60px;width:820px;height:525px;background:radial-gradient(ellipse at 50% 45%,#c9b49e 0%,#9aa6b8 35%,#d4d7dd 75%,transparent 100%)}
.brand{position:absolute;left:32px;top:40px;display:flex;align-items:center;gap:12px;font-size:20px;font-weight:600;color:var(--ink);letter-spacing:1px}
.brand-mark{width:18px;height:18px;background:var(--ink)}
.nav{position:absolute;left:318px;top:30px;font-size:15px;color:var(--ink)}
.nav a{color:inherit;text-decoration:none;position:absolute;white-space:nowrap}
.nav a.active::after{content:"";position:absolute;left:0;right:0;bottom:-12px;height:3px;background:var(--red)}
.hero .login{left:1065px;top:25px;width:110px;height:36px;font-size:15px}
.hero h1{position:absolute;left:55px;top:205px;font-size:26px;font-weight:600;color:var(--ink);line-height:33px;width:400px}
.hero p{position:absolute;left:55px;top:279px;font-size:15px;line-height:23px;color:var(--muted);width:320px}
.hero .advice{left:55px;top:386px;width:174px;height:40px}

/* services */
.services{position:absolute;top:585px;left:0;width:1200px;height:416px;background:var(--white)}
.service{position:absolute;top:82px;width:240px;text-align:center}
.service svg{display:block;margin:0 auto}
.service h3{font-size:15px;font-weight:700;color:var(--ink);margin-top:58px}
.service p{font-size:14px;line-height:24px;margin-top:12px;color:var(--text)}

/* band */
.band{position:absolute;top:1001px;left:0;width:1200px;height:224px;background:linear-gradient(100deg,#4a2a22 0%,#2a2a2a 20%,#3d3d3d 45%,#6b6b6b 70%,#3a3a3a 100%)}
.band p{position:absolute;left:304px;top:96px;font-size:24px;color:var(--white)}
.band .btn{left:979px;top:90px;width:174px;height:44px}

/* who */
.who{position:absolute;top:1225px;left:0;width:1200px;height:787px}
.who h2{position:absolute;left:95px;top:127px;font-size:29px;font-weight:600;color:var(--ink)}
.who .copy{position:absolute;left:95px;top:208px;width:420px;font-size:15px;line-height:25px;color:var(--text)}
.who .copy p{margin-bottom:25px}
.who .btn{left:95px;top:600px;width:176px;height:42px}
.who-photo{position:absolute;left:620px;top:82px;width:535px;height:598px;background:linear-gradient(180deg,#dfe4ea 0%,#c7cdd6 45%,#8c939c 75%,#d9dde2 100%)}

/* team */
.team{position:absolute;top:2012px;left:0;width:1200px;height:491px;background:var(--pale)}
.team h2{position:absolute;left:95px;top:40px;font-size:24px;font-weight:700;color:var(--ink)}
.arrow{position:absolute;top:57px;width:20px;height:20px;display:flex;align-items:center;justify-content:center}
.arrow.prev{left:966px;background:#f3c9ca}
.arrow.next{left:994px;background:var(--red)}
.member{position:absolute;top:122px;width:229px;height:281px;background:var(--card);text-align:center}
.member .photo{width:135px;height:135px;margin:27px auto 0;background:linear-gradient(160deg,#d6d0c8,#8b8378)}
.member h3{font-size:18px;font-weight:400;color:var(--ink);margin-top:20px}
.member span{display:block;font-size:14px;color:var(--ink);margin-top:4px}
.member .more{position:absolute;left:96px;bottom:-18px;width:37px;height:37px;border-radius:50%;background:var(--white);display:flex;align-items:center;justify-content:center}

/* what we do */
.what{position:absolute;top:2503px;left:0;width:1200px;height:694px}
.what h2{position:absolute;left:95px;top:95px;font-size:24px;font-weight:700;color:var(--ink)}
.offer{position:absolute;top:214px;width:174px;text-align:center}
.offer .photo{width:174px;height:139px;background:linear-gradient(150deg,#e9ecef,#b7bfc8 60%,#6e7a88)}
.offer h3{font-size:21px;font-weight:600;color:var(--ink);margin-top:20px;line-height:27px}
.offer p{font-size:14px;line-height:24px;margin-top:14px;color:var(--text)}
.what .btn{left:513px;top:577px;width:174px;height:40px}

/* partners */
.partners{position:absolute;top:3197px;left:0;width:1200px;height:229px;background:var(--red);color:var(--white)}
.partners h2{position:absolute;left:0;right:0;top:32px;text-align:center;font-size:15px;font-weight:400;letter-spacing:.5px}
.partner{position:absolute;top:128px;font-size:26px;font-weight:600;white-space:nowrap}

/* footer */
.footer{position:absolute;top:3426px;left:0;width:1200px;height:254px;background:var(--foot)}
.foot-links{position:absolute;top:62px;left:152px;font-size:17px;color:var(--ink)}
.foot-links a{position:absolute;color:inherit;text-decoration:none;white-space:nowrap}
.social{position:absolute;top:66px;left:950px;display:flex;gap:22px}
.social i{display:block;width:14px;height:14px;border-radius:50%;background:var(--ink)}
.foot-line{position:absolute;top:110px;left:95px;width:1010px;height:1px;background:#c4c4c8}
.foot-brand{position:absolute;top:168px;left:0;right:0;text-align:center;font-size:18px;font-weight:600;color:var(--ink);letter-spacing:1px}
.copyright{position:absolute;top:3680px;left:0;width:1200px;height:54px;background:var(--bar);color:var(--white);font-size:14px;display:flex;align-items:center;justify-content:center}
</style>
</head>
<body>

<header class="hero">
  <div class="hero-photo" role="img" aria-label="Photo of three colleagues smiling around a laptop showing a spreadsheet"></div>
  <div class="brand"><span class="brand-mark"></span>QUORVEL ADVISERS</div>
  <nav class="nav">
    <a class="active" style="left:0">What we do</a>
    <a style="left:115px">How we do it</a>
    <a style="left:237px">Who are we</a>
    <a style="left:350px">Why use us?</a>
    <a style="left:466px">Clients</a>
    <a style="left:546px">Partners</a>
    <a style="left:638px">Contact us</a>
  </nav>
  <a class="btn login">Login</a>
  <h1>Because Money Dosen’t Come with Instructions</h1>
  <p>Since founding Quorvel Advisers in 2014 we have dedicated ourselves to the provision of services.</p>
  <a class="btn advice">Get advice</a>
</header>

<section class="services">
  <div class="service" style="left:154px">
    <svg width="100" height="100" viewBox="0 0 100 100" fill="none" stroke="#999" stroke-width="2"><path d="M2 16V2h14M84 2h14v14M98 84v14H84M16 98H2V84"/><path d="M30 66c8-2 14 4 22 2l16-8M40 46l10-8 8 6 12-12" stroke="#888"/><rect x="26" y="60" width="6" height="16" fill="#999"/></svg>
    <h3>Financial Planning</h3>
    <p>At vero eos et accusamus<br>et iusto odio dignissimos<br>ducimus qui blanditiis</p>
  </div>
  <div class="service" style="left:373px">
    <svg width="100" height="100" viewBox="0 0 100 100" fill="none" stroke="#999" stroke-width="2"><path d="M2 16V2h14M84 2h14v14M98 84v14H84M16 98H2V84"/><circle cx="50" cy="30" r="6"/><path d="M42 42h16v24h-4v14h-8V66h-4z"/></svg>
    <h3>Retirement Planning</h3>
    <p>At vero eos et accusamus<br>et iusto odio dignissimos<br>ducimus qui blanditiis</p>
  </div>
  <div class="service" style="left:590px">
    <svg width="100" height="100" viewBox="0 0 100 100" fill="none" stroke="#f04a50" stroke-width="2.5"><path d="M2 16V2h14M84 2h14v14M98 84v14H84M16 98H2V84"/><path d="M50 26L74 70H26z" stroke-width="4" stroke-linejoin="round"/><path d="M50 40v16M50 61v4" stroke-width="4"/></svg>
    <h3>Risk Management</h3>
    <p>At vero eos et accusamus<br>et iusto odio dignissimos<br>ducimus qui blanditiis</p>
  </div>
  <div class="service" style="left:806px">
    <svg width="100" height="100" viewBox="0 0 100 100" fill="none" stroke="#999" stroke-width="2"><path d="M2 16V2h14M84 2h14v14M98 84v14H84M16 98H2V84"/><rect x="34" y="22" width="32" height="44"/><path d="M40 32h20M40 42h20M40 52h12"/></svg>
    <h3>Taxation</h3>
    <p>At vero eos et accusamus<br>et iusto odio dignissimos<br>ducimus qui blanditiis</p>
  </div>
</section>

<section class="band" role="img" aria-label="Close-up photo of a financial statement with figures">
  <p>we provide expert advice for business &amp; individuals</p>
  <a class="btn">Get service</a>
</section>

<section class="who">
  <h2>Who are we</h2>
  <div class="copy">
    <p>Since founding Quorvel Advisers in 2014 we have dedicated ourselves to the provision of services.</p>
    <p>What differentiates us from other advisers or consultancies is a genuine motivation to see our clients succeed.<br>Today’s technology allows our clients to take their knowledge to the market in ways that previous generations could only dream</p>
    <p>That’s why Quorvel is dedicated to seeing you choose the right technology strategy</p>
  </div>
  <a class="btn">Read more</a>
  <div class="who-photo" role="img" aria-label="Photo of business people by a window with glasses on a desk"></div>
</section>

<section class="team">
  <h2>Our expert team</h2>
  <span class="arrow prev"><svg width="8" height="10" viewBox="0 0 8 10"><path d="M6 1L2 5l4 4" stroke="#f04a50" stroke-width="2" fill="none"/></svg></span>
  <span class="arrow next"><svg width="8" height="10" viewBox="0 0 8 10"><path d="M2 1l4 4-4 4" stroke="#fff" stroke-width="2" fill="none"/></svg></span>
  <div class="member" style="left:102px"><div class="photo" role="img" aria-label="Portrait of Tom Ashworth"></div><h3>Tom Ashworth</h3><span>Director</span><span class="more"><svg width="8" height="10" viewBox="0 0 8 10"><path d="M2 1l4 4-4 4" stroke="#333" stroke-width="1.5" fill="none"/></svg></span></div>
  <div class="member" style="left:344px"><div class="photo" role="img" aria-label="Portrait of Elena Hart"></div><h3>Elena Hart</h3><span>Director</span><span class="more"><svg width="8" height="10" viewBox="0 0 8 10"><path d="M2 1l4 4-4 4" stroke="#333" stroke-width="1.5" fill="none"/></svg></span></div>
  <div class="member" style="left:588px"><div class="photo" role="img" aria-label="Portrait of Ray Colburn"></div><h3>Ray Colburn</h3><span>Director</span><span class="more"><svg width="8" height="10" viewBox="0 0 8 10"><path d="M2 1l4 4-4 4" stroke="#333" stroke-width="1.5" fill="none"/></svg></span></div>
  <div class="member" style="left:832px"><div class="photo" role="img" aria-label="Portrait of Simon Pell"></div><h3>Simon Pell</h3><span>Director</span><span class="more"><svg width="8" height="10" viewBox="0 0 8 10"><path d="M2 1l4 4-4 4" stroke="#333" stroke-width="1.5" fill="none"/></svg></span></div>
</section>

<section class="what">
  <h2>What we do</h2>
  <div class="offer" style="left:162px"><div class="photo" role="img" aria-label="Photo of colleagues reviewing reports at a desk"></div><h3>Research</h3><p>topical paper white labelled and sponsored article</p></div>
  <div class="offer" style="left:393px"><div class="photo" role="img" aria-label="Photo of a presenter training a group at a whiteboard"></div><h3>Training</h3><p>Trading technology for compliance and non technical staff</p></div>
  <div class="offer" style="left:625px"><div class="photo" role="img" aria-label="Photo of a team meeting around a table"></div><h3>Product Devlopment</h3><p>Trading technology for compliance and non technical staff</p></div>
  <div class="offer" style="left:857px"><div class="photo" role="img" aria-label="Photo of an adviser meeting a client"></div><h3>Advice</h3><p>Board level advisory and programme management</p></div>
  <a class="btn">Explore more</a>
</section>

<section class="partners">
  <h2>OUR AWESOME PARTNERS</h2>
  <span class="partner" style="left:22px">Northvale</span>
  <span class="partner" style="left:262px">Brightmere Group</span>
  <span class="partner" style="left:580px">Lindqvist Net</span>
  <span class="partner" style="left:912px">Kestrelon</span>
</section>

<footer class="footer">
  <div class="foot-links">
    <a style="left:0">About</a>
    <a style="left:92px">Legal Information</a>
    <a style="left:280px">Contact</a>
    <a style="left:386px">Terms &amp; Services</a>
    <a style="left:570px">Privacy Policy</a>
  </div>
  <div class="social"><i></i><i></i><i></i><i></i></div>
  <div class="foot-line"></div>
  <div class="foot-brand">QUORVEL ADVISERS</div>
</footer>
<div class="copyright">©2017 All Right Reserved</div>

</body>
</html>
```